need a clean, modern job advertisement designed for social media (Facebook & Instagram).

The post is to advertise two positions:
• Leading Hand Boilermaker
• Dragline Fitter
We want the design to match our KRT Plant Services branding: blue, white, strong, professional, mining-industry style.
What the design should include:
Bold headline: “WE’RE HIRING”
Sub-headline: “Leading Hand Boilermaker & Dragline Fitter”
Key points:
• Bowen Basin based
• Dragline & shovel maintenance
• Great pay + long-term work
• Locally owned & operated
KRT logo placed cleanly
Space for 1–2 images (boilermaking or dragline work)
Design style:
Strong and industrial
Blue/white colour scheme
Easy to read at a glance
Suitable for a square 1080×1080 design

```html
<!DOCTYPE html>
<html lang="en">
<head>
<meta charset="utf-8">
<title>KRT Plant Services – We're Hiring</title>
<link rel="stylesheet" href="https://fonts.googleapis.com/css2?family=Oswald:wght@700&family=Poppins:wght@600;700;800&display=swap">
<style>
  :root {
    --ink: #111214;
    --night: #1a1b1e;
    --white: #ffffff;
    --blue-deep: #0757d6;
    --blue: #0a86ea;
    --blue-light: #1cb4f5;
    --cyan: #1fd0f4;
    --navy-text: #0b2350;
    --photo-a: #1b2446;
    --photo-b: #4a5676;
  }
  * { box-sizing: border-box; margin: 0; padding: 0; }
  html, body { width: 1200px; height: 1200px; overflow: hidden; background: #c4c4c4; }
  .post {
    position: relative; width: 1200px; height: 1200px; overflow: hidden;
    font-family: "Poppins", sans-serif; color: var(--ink);
  }
  .post__art { position: absolute; inset: 0; }
  .brand {
    position: absolute; left: 96px; top: 150px;
    display: flex; align-items: center; gap: 14px;
    font-weight: 700; font-size: 30px; color: var(--white); letter-spacing: 0.5px;
  }
  .brand__dot { width: 26px; height: 26px; border-radius: 50%; background: var(--blue-light); }
  .headline__tag {
    position: absolute; left: 85px; top: 289px; width: 292px; height: 85px;
    background: var(--blue); border-radius: 14px;
    font-family: "Oswald", sans-serif; font-weight: 700; font-size: 70px; line-height: 85px;
    color: var(--white); padding-left: 16px; letter-spacing: 1px;
  }
  .headline__tag::after {
    content: ""; position: absolute; left: 254px; bottom: -22px;
    border-left: 22px solid transparent; border-top: 24px solid var(--blue);
  }
  .headline__main {
    position: absolute; left: 80px; top: 350px;
    font-family: "Oswald", sans-serif; font-weight: 700; font-size: 206px; line-height: 1;
    letter-spacing: 1px;
    background: linear-gradient(180deg, var(--blue-deep) 0%, var(--blue) 55%, var(--blue-light) 100%);
    -webkit-background-clip: text; background-clip: text; color: transparent;
  }
  .roles {
    position: absolute; left: 85px; top: 570px;
    font-weight: 700; font-size: 55px; line-height: 64px; color: var(--ink);
  }
  .location {
    position: absolute; left: 118px; top: 803px; width: 989px; height: 79px;
    background: linear-gradient(90deg, var(--ink) 0%, var(--ink) 60%, #777 88%, var(--white) 100%);
    border-radius: 0 8px 8px 0;
    font-weight: 700; font-size: 64px; line-height: 79px; color: var(--white); padding-left: 46px;
  }
  .location__pin { position: absolute; left: 86px; top: 806px; }
  .perks { position: absolute; left: 86px; top: 907px; display: flex; gap: 17px; }
  .perk {
    position: relative; width: 330px; height: 97px; border-radius: 10px;
    background: linear-gradient(180deg, var(--blue-light), var(--blue-deep));
    font-weight: 700; font-size: 30px; line-height: 36px; color: var(--white);
    padding: 10px 0 0 42px;
  }
  .perk__tick { position: absolute; left: 12px; top: 18px; }
  .cta {
    position: absolute; left: 98px; top: 1078px;
    font-weight: 700; font-size: 31px; line-height: 50px; color: var(--white);
  }
  .cta__mail {
    position: absolute; left: 651px; top: 1077px; width: 480px; height: 53px;
    background: var(--blue-light); border-radius: 10px;
    display: flex; align-items: center; gap: 14px; padding-left: 14px;
    font-weight: 700; font-size: 26px; color: var(--navy-text);
  }
  .cta__mail strong { font-weight: 700; margin-left: 6px; }
</style>
</head>
<body>
<main class="post">
  <svg class="post__art" width="1200" height="1200" viewBox="0 0 1200 1200" aria-hidden="false">
    <defs>
      <linearGradient id="topBg" x1="0" y1="0" x2="1" y2="1">
        <stop offset="0" stop-color="#2a2b2e"/><stop offset="1" stop-color="#121214"/>
      </linearGradient>
      <linearGradient id="photoTone" x1="0" y1="0" x2="1" y2="1">
        <stop offset="0" stop-color="var(--photo-a)"/><stop offset="1" stop-color="var(--photo-b)"/>
      </linearGradient>
      <linearGradient id="photoLight" x1="0" y1="0" x2="1" y2="1">
        <stop offset="0" stop-color="#c9ccd2"/><stop offset="1" stop-color="#6c6f77"/>
      </linearGradient>
      <linearGradient id="photoSparks" x1="0" y1="0" x2="1" y2="1">
        <stop offset="0" stop-color="#3b3128"/><stop offset="1" stop-color="#16171c"/>
      </linearGradient>
    </defs>
    <!-- backdrop bands -->
    <rect class="band band--top" width="1200" height="1200" fill="url(#topBg)"/>
    <polygon class="band band--light" points="0,245 475,245 1200,715 1200,953 0,953" fill="var(--white)"/>
    <polyline class="band__rule" points="0,252 470,252 800,466" fill="none" stroke="var(--cyan)" stroke-width="7"/>
    <rect class="band band--base" y="953" width="1200" height="247" fill="var(--ink)"/>

    <!-- feature photo -->
    <g role="img" aria-label="Boilermaker in a welding helmet welding inside a dragline structure">
      <polygon points="710,118 945,1 1183,123 1183,402 945,519 710,402" fill="var(--white)"/>
      <polygon points="722,125 945,13 1171,130 1171,395 945,506 722,395" fill="url(#photoTone)"/>
    </g>
    <!-- crew photo -->
    <g role="img" aria-label="Fitters in hi-vis working on scaffolding beside a dragline boom">
      <polyline points="676,698 808,768 940,698" fill="none" stroke="var(--cyan)" stroke-width="5"/>
      <polygon points="808,478 933,539 933,691 808,757 683,691 683,539" fill="var(--white)"/>
      <polygon points="808,490 923,546 923,684 808,745 693,684 693,546" fill="url(#photoLight)"/>
    </g>
    <!-- grinding photo -->
    <g role="img" aria-label="Tradesman grinding steel with sparks inside a machine">
      <polyline points="940,698 1075,773 1200,706" fill="none" stroke="var(--cyan)" stroke-width="5"/>
      <polygon points="1075,478 1200,539 1200,701 1075,762 950,691 950,539" fill="var(--white)"/>
      <polygon points="1075,490 1200,551 1200,690 1075,750 960,684 960,546" fill="url(#photoSparks)"/>
    </g>
  </svg>

  <div class="brand"><span class="brand__dot"></span>KRT Plant Services</div>

  <div class="headline__tag">WE’RE</div>
  <h1 class="headline__main">HIRING</h1>

  <h2 class="roles">Leading Hand<br>Boilermaker &amp;<br>Dragline Fitter</h2>

  <div class="location">Bowen Basin based</div>
  <svg class="location__pin" width="54" height="76" viewBox="0 0 54 76" aria-hidden="true">
    <path d="M27 2C13 2 2 13 2 27c0 18 25 47 25 47s25-29 25-47C52 13 41 2 27 2z" fill="var(--blue)" stroke="var(--white)" stroke-width="3"/>
    <circle cx="27" cy="26" r="9" fill="var(--white)"/>
    <circle cx="27" cy="26" r="4" fill="var(--blue)"/>
  </svg>

  <ul class="perks">
    <li class="perk"><svg class="perk__tick" width="22" height="22" viewBox="0 0 22 22" aria-hidden="true"><circle cx="11" cy="11" r="10" fill="var(--ink)"/><path d="M6 11l3.5 3.5L16 8" fill="none" stroke="var(--white)" stroke-width="2.5"/></svg>Dragline &amp; shovel<br>maintenance</li>
    <li class="perk" style="padding-left:52px"><svg class="perk__tick" width="22" height="22" viewBox="0 0 22 22" aria-hidden="true"><circle cx="11" cy="11" r="10" fill="var(--ink)"/><path d="M6 11l3.5 3.5L16 8" fill="none" stroke="var(--white)" stroke-width="2.5"/></svg>Great pay +<br>long-term work</li>
    <li class="perk" style="padding-left:52px"><svg class="perk__tick" width="22" height="22" viewBox="0 0 22 22" aria-hidden="true"><circle cx="11" cy="11" r="10" fill="var(--ink)"/><path d="M6 11l3.5 3.5L16 8" fill="none" stroke="var(--white)" stroke-width="2.5"/></svg>Locally owned<br>&amp; operated</li>
  </ul>

  <p class="cta">APPLY NOW or find out more by</p>
  <p class="cta__mail">emailing
    <svg width="32" height="30" viewBox="0 0 32 30" aria-hidden="true"><rect x="2" y="10" width="28" height="18" rx="2" fill="var(--navy-text)"/><path d="M2 11l14 10 14-10" fill="none" stroke="var(--blue-light)" stroke-width="2.5"/><rect x="9" y="2" width="14" height="11" fill="var(--white)"/></svg>
    <strong>admin@krt.net.au</strong></p>
</main>
</body>
</html>
```